Digital Marketing Agency Landing Page

At VELMIT, we offer a comprehensive solution for solar companies' client acquisition needs in the rapidly growing industry. We handle end-to-end client acquisition, meaning we manage the entire lifecycle of capturing new clients—from initial lead generation to delivering the ready-to-buy homeowner. Our expertise in targeted advertising, data analytics, and customer relationship management ensures that we not only find potential customers but also nurture them through tailored engagement strategies until they are ready to make a purchase. By entrusting us with your client acquisition process, solar companies can focus on what they do best—providing sustainable energy solutions—while we work behind the scenes to grow your customer base and increase your market share.

We need to restructure our website to make it more professional. We don't need any complex functionalities. We are looking for someone that is good in design and can build a visually aesthetic website following our brand image. We only need a landing page and a lead form in the end. I would like to have only one page, but a relatively big one where people scroll down. I would like to have a minimal and classy look. Something that is timeless and elegant.

Structure:

initial page
About us
How we operate
Get in touch

Target Market(s)

Solar Comapanies

Industry/Entity Type

Marketing solautions

Coding

Coded - Design and coding required

Number of Pages Required

1 page

Requirements
Nice to have
• Inspirations: https://www.qz.lo/ https://www.junebrook.example/ https://www.megaroster.example/ https://pluno.example/

```html
<!DOCTYPE html>
<html lang="en">
<head>
<meta charset="utf-8">
<title>VELMIT — Solar Client Acquisition</title>
<link href="https://fonts.googleapis.com/css2?family=Montserrat:wght@300;400;500;600&display=swap" rel="stylesheet">
<style>
:root{
  --navy:#0f222d;
  --sand:#ebe7d9;
  --paper:#ebeae5;
  --stage:#dcd9cb;
  --rule:#9aa0a2;
  --muted:#5c6468;
  --sky-light:#d4d3cc;
  --sky-mid:#9a9e9c;
  --steel:#6b7274;
  --shadow:#3f4549;
}
*{box-sizing:border-box;margin:0;padding:0}
html,body{width:1200px;height:3528px;overflow:hidden}
body{background:var(--stage);font-family:"Montserrat",sans-serif;color:var(--navy);position:relative}
.page{position:absolute;left:222px;top:279px;width:792px;height:3146px;background:var(--paper);overflow:hidden}
.photo{position:absolute}
.photo-hero{background:linear-gradient(180deg,var(--sky-light) 0%,#c4c3bb 38%,#8e918f 62%,#5b5f61 82%,var(--shadow) 100%)}
.photo-wind{background:linear-gradient(180deg,#7b817f 0%,#a9adaa 45%,#8d9291 70%,#4f565a 85%,#3a4246 100%)}
.photo-tech{background:linear-gradient(120deg,#3d4448 0%,#6c7374 30%,#c9cac5 55%,#8a8f8f 75%,#464d51 100%)}
.photo-team{background:linear-gradient(160deg,#555c5f 0%,#a6a9a6 35%,#d7d7d1 60%,#7c8283 85%,#474e52 100%)}
.photo-consult{background:linear-gradient(180deg,#7d8384 0%,#b8bab5 40%,#d0d0ca 65%,#6d7375 100%)}
.photo-laptop{background:linear-gradient(150deg,#aeb0ab 0%,#d8d8d2 40%,#8f9393 65%,#4c5356 100%)}
.photo-roof{background:linear-gradient(180deg,#4b5256 0%,#8c9090 30%,#c6c7c1 55%,#6a7072 80%,#3c4347 100%)}
.photo-aerial{background:linear-gradient(135deg,#5a6163 0%,#8e9392 40%,#4a5155 70%,#767c7d 100%)}
.rule{position:absolute;left:0;width:792px;height:1px;background:var(--rule)}

.nav{position:absolute;left:0;top:0;width:792px;height:47px;border-bottom:1px solid var(--rule)}
.brand{position:absolute;left:74px;top:11px;width:64px;height:23px;border:1px solid var(--navy);font-size:11px;font-weight:400;letter-spacing:.4px;display:flex;align-items:center;justify-content:center}
.nav-link{position:absolute;top:19px;font-size:6.5px;color:var(--navy)}
.nav-divider{position:absolute;left:499px;top:0;width:1px;height:47px;background:var(--rule)}
.nav-contact{position:absolute;right:74px;top:19px;font-size:6.5px}

.section-label{position:absolute;left:77px;font-size:6px;letter-spacing:.5px;color:var(--muted);writing-mode:vertical-rl;transform:rotate(180deg);text-transform:uppercase}
.heading{position:absolute;left:199px;font-weight:400;color:var(--navy);white-space:nowrap}
.hero-title{top:102px;font-size:26.5px;line-height:32px;letter-spacing:.1px}
.h2{font-size:22px;line-height:26.5px}

.btn-outline{position:absolute;left:608px;top:160px;width:110px;height:30px;border:1px solid var(--navy);font-size:6.5px;font-weight:600;display:flex;align-items:center;justify-content:center;gap:5px}
.corner-block{position:absolute;left:0;top:570px;width:74px;height:75px;background:var(--navy)}
.corner-mark{position:absolute;left:24px;top:25px;width:26px;height:26px;border:1px solid var(--sand)}

.stat{position:absolute;width:180px}
.stat-num{font-size:21px;font-weight:400;margin-bottom:6px}
.stat-text{font-size:6.3px;line-height:13px;color:var(--muted)}

.about-copy{position:absolute;left:552px;top:966px;width:168px;font-size:6.5px;line-height:13.3px;color:var(--muted)}
.about-copy p+p{margin-top:13px}

.case{position:absolute;top:2382px;width:297px}
.case .photo{position:relative;width:297px;height:195px}
.case-date{font-size:5.5px;color:var(--muted);margin-top:12px}
.case-title{font-size:13px;font-weight:400;margin-top:4px;white-space:nowrap}

.contact-panel{position:absolute;left:74px;top:2829px;width:718px;height:317px;background:var(--navy);color:var(--sand)}
.contact-intro{position:absolute;left:125px;top:59px;width:200px;font-size:12px;line-height:18px;font-weight:300}
.contact-line{position:absolute;left:124px;width:180px;height:1px;background:#4a5860}
.contact-info{position:absolute;left:124px;top:158px;font-size:8.5px;font-weight:300;white-space:nowrap}
.field{position:absolute;left:411px;width:233px;font-size:7px;font-weight:300;padding-bottom:10px;border-bottom:1px solid #3b4b54}
.btn-submit{position:absolute;left:411px;top:252px;width:123px;height:25px;background:var(--sand);color:var(--navy);font-size:6.5px;font-weight:600;display:flex;align-items:center;justify-content:center;gap:5px}
</style>
</head>
<body>
<main class="page">

  <header class="nav">
    <div class="brand">VELMIT</div>
    <span class="nav-link" style="left:199px">About</span>
    <span class="nav-link" style="left:256px">How We Operate</span>
    <span class="nav-link" style="left:352px">Get in Touch</span>
    <span class="nav-divider"></span>
    <span class="nav-contact">+1 555 010 2040 &nbsp;|&nbsp; hello@velmit.example</span>
  </header>

  <section class="hero">
    <h1 class="heading hero-title">Bridging the Gap between<br>the Solar Experts and<br>Value-Driven Homeowners</h1>
    <div class="btn-outline">How We Operate
      <svg width="9" height="6" viewBox="0 0 9 6"><path d="M0 3h8M5.5 .5 8 3 5.5 5.5" fill="none" stroke="currentColor" stroke-width=".8"/></svg>
    </div>
    <div class="photo photo-hero" style="left:74px;top:249px;width:718px;height:396px" role="img" aria-label="Two engineers in hard hats walking between rows of solar panels"></div>
    <div class="corner-block"><span class="corner-mark"></span></div>
  </section>

  <section class="intro">
    <span class="section-label" style="top:697px">Intro</span>
    <div class="stat" style="left:292px;top:703px">
      <div class="stat-num">500+</div>
      <p class="stat-text">VELMIT has successfully served over 500 solar companies with its comprehensive solutions.</p>
    </div>
    <div class="stat" style="left:540px;top:703px">
      <div class="stat-num">150</div>
      <p class="stat-text">Their expertise have contributed to the successful launch of 150 new solar ventures.</p>
    </div>
    <div class="stat" style="left:292px;top:795px">
      <div class="stat-num">246</div>
      <p class="stat-text">Comprehensive solutions to 246 companies, helping them enhance their performance</p>
    </div>
    <div class="stat" style="left:540px;top:795px">
      <div class="stat-num">37%</div>
      <p class="stat-text">VELMIT's expertise has led to a 37% increase in efficiency for numerous solar projects</p>
    </div>
  </section>
  <div class="rule" style="top:908px"></div>

  <section class="about">
    <span class="section-label" style="top:970px">About</span>
    <h2 class="heading h2" style="top:964px">At VELMIT, we offer a<br>comprehensive solution<br>for solar companies' client<br>acquisition needs in the<br>rapidly growing industry.</h2>
    <div class="about-copy">
      <p>Our expertise in targeted advertising, and customer relationship management ensures that we not only find potential customers but also nurture them through tailored engagement strategies until they are ready to make a purchase.</p>
      <p>By entrusting us with client acquisition process, solar companies can focus on what they do best—providing sustainable energy solutions—while we work behind the scenes to grow your customer base and increase your market share.</p>
    </div>
    <div class="photo photo-wind" style="left:199px;top:1182px;width:519px;height:247px" role="img" aria-label="Wind turbines rising behind a field of solar panels"></div>
  </section>
  <div class="rule" style="top:1488px"></div>

  <section class="operate">
    <span class="section-label" style="top:1549px">How we operate</span>
    <h2 class="heading h2" style="top:1543px">Providing sustainable energy<br>solutions—while we work behind<br>the scenes to grow your customer<br>base and increase your market</h2>
    <div class="photo photo-tech" style="left:199px;top:1688px;width:519px;height:197px" role="img" aria-label="Technician with a tablet inspecting solar panels"></div>
    <div class="photo photo-team" style="left:199px;top:1906px;width:345px;height:148px" role="img" aria-label="Team reviewing a small solar and wind model on a table"></div>
    <div class="photo photo-consult" style="left:563px;top:1906px;width:137px;height:212px" role="img" aria-label="Consultant in a light shirt talking with a colleague"></div>
  </section>
  <div class="rule" style="top:2203px"></div>

  <section class="cases">
    <span class="section-label" style="top:2262px">Case studies</span>
    <h2 class="heading h2" style="top:2257px">Explore some of the most<br>recent case studies we’ve<br>worked on</h2>
    <article class="case" style="left:74px">
      <div class="photo photo-laptop" role="img" aria-label="Hands typing on a laptop beside a coffee cup"></div>
      <p class="case-date">September 25, 2023</p>
      <h3 class="case-title">How the Market is Expanding</h3>
    </article>
    <article class="case" style="left:386px">
      <div class="photo photo-roof" role="img" aria-label="Installer carrying a solar panel on a rooftop"></div>
      <p class="case-date">September 25, 2023</p>
      <h3 class="case-title">How Efficient are Solar Panels</h3>
    </article>
    <article class="case" style="left:698px">
      <div class="photo photo-aerial" role="img" aria-label="Aerial view of rooftops with solar arrays"></div>
      <p class="case-date">September 25, 2023</p>
      <h3 class="case-title">How Efficient are Solar Panels</h3>
    </article>
  </section>
  <div class="rule" style="top:2655px"></div>

  <section class="contact">
    <span class="section-label" style="top:2734px">Contact us</span>
    <h2 class="heading h2" style="top:2730px">Have a project in mind?<br>Let’s get in touch</h2>
    <div class="contact-panel">
      <p class="contact-intro">Let’s work together. You can either fill the inquiry form or contact us via phone</p>
      <span class="contact-line" style="top:128px"></span>
      <p class="contact-info">hello@velmit.example &nbsp;•&nbsp; +1 555 010 2040</p>
      <span class="contact-line" style="top:188px"></span>
      <div class="field" style="top:61px">Company name</div>
      <div class="field" style="top:99px">Phone Number</div>
      <div class="field" style="top:136px">Email Address</div>
      <div class="field" style="top:174px">City</div>
      <div class="field" style="top:211px">Inquiry</div>
      <div class="btn-submit">Submit Your Inquiry
        <svg width="9" height="6" viewBox="0 0 9 6"><path d="M0 3h8M5.5 .5 8 3 5.5 5.5" fill="none" stroke="currentColor" stroke-width=".8"/></svg>
      </div>
    </div>
  </section>

</main>
</body>
</html>
```